RT Consult - Web Design Upgrade

We have recently designed a website (http://www.rtconsult-demo.com.au) which requires more creative and professional inputs. The website was designed using 'jolly portals site builder template' and it is currently available for viewing on the internet. Also, you are able to access the PDF files for the 6 main pages (i.e. Home, About, Services, Contaminated Land Management, Groundwater Management and Contact).

The current website has 17 pages, however, your design may only be required for the 6 main pages.

Currently the website background is white but we are open to other colours provided the company logo is adjusted accordingly.

The idea is to upgrade the existing design and, if possible, continue using 'jolly portals' as the preferred web host. So we are not sure if the design should be coded or uncoded...we leave it to your proficiency and advice.

Target Market(s)

Government organisations, landowners and developers, waste and utilities companies, community organisations and individuals.

Industry/Entity Type

Internet

Number of Pages Required

5+ page

Font styles to use
Sans Serif

Colors
0355a3
3176b5
9ccb3b
acd037
ffffff

Requirements
Nice to have
• Sliding images

```html
<!DOCTYPE html>
<html lang="en">
<head>
<meta charset="utf-8">
<title>RT Consult – Contact</title>
<link href="https://fonts.googleapis.com/css2?family=Arimo:wght@400;700&display=swap" rel="stylesheet">
<style>
  :root{
    --brand-blue:#0355a3;
    --mid-blue:#3176b5;
    --brand-green:#9ccb3b;
    --lime:#acd037;
    --white:#ffffff;
    --navy-heading:#1f3a6b;
    --body-text:#333333;
    --band-grey:#ececec;
    --field-border:#dcdcdc;
    --placeholder:#a8a8a8;
    --map-base:#e9e4d8;
  }
  *{box-sizing:border-box;margin:0;padding:0}
  html,body{width:1108px;height:1200px;overflow:hidden;background:var(--white)}
  body{position:relative;font-family:"Arimo",Helvetica,Arial,sans-serif;color:var(--body-text)}
  .abs{position:absolute}

  /* header */
  .brand{left:113px;top:40px;display:flex;align-items:center;gap:10px}
  .brand-dot{width:34px;height:34px;border-radius:50%;background:var(--brand-blue)}
  .brand-name{font-size:24px;font-weight:700;color:var(--brand-blue);letter-spacing:.5px}
  .tagline{right:113px;top:46px;font-size:24px;color:var(--brand-green);letter-spacing:1px;white-space:nowrap}

  /* nav */
  .main-nav{left:0;top:115px;width:1108px;height:56px;background:var(--brand-blue)}
  .nav-item{top:0;height:56px;line-height:56px;color:var(--white);font-size:16px;font-weight:700;letter-spacing:.4px;text-decoration:none}
  .nav-item.is-active{background:var(--brand-green);width:93px;text-align:center}
  .search{left:682px;top:13px;width:314px;height:26px;background:var(--white);border-radius:6px;overflow:hidden}
  .search-field{left:10px;top:0;line-height:26px;font-size:13px;font-style:italic;color:#555;letter-spacing:.4px}
  .search-go{right:0;top:0;width:66px;height:26px;background:var(--brand-green);color:var(--white);font-weight:700;font-size:13px;text-align:center;line-height:26px;border-radius:6px}

  /* page title band */
  .title-band{left:0;top:171px;width:1108px;height:70px;background:var(--band-grey)}
  .page-title{left:112px;top:22px;font-size:24px;color:var(--navy-heading);letter-spacing:1px;font-weight:400}

  /* map */
  .location-map{left:111px;top:267px;width:884px;height:294px;border:2px solid #dadada;background:linear-gradient(100deg,var(--map-base) 0%,#e6e1cf 45%,#ece7d9 75%,#aac8ee 100%)}

  .intro{left:112px;top:576px;width:886px;font-size:13px;line-height:15.7px;letter-spacing:.5px}

  /* contact details */
  .contact-line{font-size:13px;line-height:15.7px;letter-spacing:.6px}
  .address{left:251px;top:673px}
  .phones{left:665px;top:676px}
  .icon-pin{left:222px;top:676px}
  .icon-phone{left:631px;top:678px}

  /* feedback */
  .section-title{left:112px;top:754px;font-size:24px;color:var(--navy-heading);letter-spacing:1px;font-weight:400}
  .field{left:109px;width:367px;height:43px;border:1px solid var(--field-border);border-radius:8px;padding:14px 18px;font-size:13px;color:var(--placeholder);letter-spacing:.6px}
  .field-message{left:493px;top:787px;width:504px;height:162px;padding-top:17px;padding-left:20px}
  .send-btn{left:878px;top:968px;width:117px;height:38px;background:var(--brand-blue);border-radius:7px;color:var(--white);font-weight:700;font-size:13.5px;letter-spacing:.6px;text-align:center;line-height:38px}

  /* footer */
  .footer-band{left:0;top:1072px;width:1108px;height:108px;background:var(--band-grey)}
  .footer{left:112px;top:12px;width:884px;height:88px;background:var(--brand-blue);color:var(--white)}
  .legal{left:22px;top:14px;font-size:13px;line-height:16px;letter-spacing:.6px}
  .footer-nav{right:28px;top:32px;font-size:13.5px;font-weight:700;letter-spacing:.5px}
  .footer-nav .sep{font-weight:400;margin:0 9px}
</style>
</head>
<body>

<header>
  <div class="abs brand"><span class="brand-dot"></span><span class="brand-name">RT Consult</span></div>
  <div class="abs tagline">″Caring for Land and Water Together″</div>
</header>

<nav class="abs main-nav">
  <a class="abs nav-item" style="left:158px">Home</a>
  <a class="abs nav-item" style="left:258px">About</a>
  <a class="abs nav-item" style="left:357px">Services</a>
  <a class="abs nav-item is-active" style="left:440px">Contact</a>
  <div class="abs search">
    <span class="abs search-field">Search...</span>
    <span class="abs search-go">Go</span>
  </div>
</nav>

<section class="abs title-band">
  <h1 class="abs page-title">How To Find Us</h1>
</section>

<div class="abs location-map" role="img" aria-label="Street map of the city area with a red marker at the office location"></div>

<p class="abs intro">Faucibus orci luctus et trices posuere cubilia Suspendisse sollicit udin velit sed leo. Ut pharetra aue nec augentum. Donec in velit vel ipsum auue. Nam elit magna Donec porta diam eu massa. Quisque diam lorem interdum vitaapibus ac scelerisque vitae pede. Donec eget tellus non erat. lacinia fermentum. Donec in velit vel ipsum auctovinar. Proin ullamcorper urna et felisstibulum iaculis lacinia est. Proin dictum elementum velit. Fusce euismod consequat ante. Lorem ipsum dolor sit met consectetuer adipiscing elit.</p>

<svg class="abs icon-pin" width="18" height="24" viewBox="0 0 18 24" aria-hidden="true">
  <path d="M9 1.5C4.9 1.5 1.8 4.6 1.8 8.6 1.8 13.6 9 22 9 22s7.2-8.4 7.2-13.4C16.2 4.6 13.1 1.5 9 1.5z" fill="none" stroke="var(--brand-blue)" stroke-width="2"/>
  <circle cx="9" cy="8.6" r="2.6" fill="none" stroke="var(--brand-blue)" stroke-width="1.8"/>
</svg>
<div class="abs contact-line address">River &amp; Terrain Consulting Pty Ltd<br>48 Harbourline Street, Marrickdale, NSW 2299</div>

<svg class="abs icon-phone" width="22" height="22" viewBox="0 0 22 22" aria-hidden="true">
  <path d="M5 1.5l3.2 4.3-2 2.4c1.3 3 3.6 5.4 6.7 6.8l2.4-2 4.3 3.2-1.8 3.3c-.5.8-1.5 1.1-2.4.8C8.6 18.3 3.7 13.4 1.7 6.6c-.3-.9 0-1.9.8-2.4z" fill="var(--brand-blue)"/>
</svg>
<div class="abs contact-line phones">+61 (0)400 555 182<br>+61 (0)2 5550 1473<br>+61 (0)2 5550 1486</div>

<h2 class="abs section-title">Feedback</h2>
<div class="abs field" style="top:787px">Name</div>
<div class="abs field" style="top:848px">Email</div>
<div class="abs field" style="top:906px">Phone</div>
<div class="abs field field-message">Message</div>
<div class="abs send-btn">Send Message</div>

<footer class="abs footer-band">
  <div class="abs footer">
    <div class="abs legal">Copyright&nbsp; 2014 - River &amp; Terrain Consulting Pty Ltd<br>Also trading as RT Consult - All rights reserved<br>ABN 00 000 000 000</div>
    <div class="abs footer-nav">Home<span class="sep">/</span>About<span class="sep">/</span>Services<span class="sep">/</span>Contact</div>
  </div>
</footer>

</body>
</html>
```